Business card logo/design needed

I need a new and fresh business card to get my name out there.
I have made plenty before and have a logo but I dont think it is sending the right message across.
I am a personal trainer running a small online business designed to cut the cost of training by taking it online, allowing you to purchase training over the net, through the help of Skype and video uploads.
You can personalized programs hand written for you or more general programs aimed at your goals.
Our goal is to get everyone to look like and behave like an athlete because there is no point in being in shape if you cant do anything with that body.
I also have a strong background in sports, having played low level college basketball in america and worked as a strength and conditioning coach. I dont like running or slow cardio, I am more focused on weights and functional training for aerobic fitness.
I am young for what I do, but I have lot of knowledge and I need something that says that I am not your standard drill sergeant trainer but someone who will truly help you reach your goals.
My curent logo text is "Train like an athlete" but I am not set on that.

Industry/Entity Type

Personal Trainer

Contact Information for Business Card

Corwin Maddock
Ironvale Motion
Personal trainer
Strength and conditioning coach
0491 572 806
www.ironvalemotion.com

```html
<!DOCTYPE html>
<html lang="en">
<head>
<meta charset="utf-8">
<title>Ironvale Motion — Business Card</title>
<link rel="stylesheet" href="https://fonts.googleapis.com/css2?family=Teko:wght@400;500&display=swap">
<style>
  :root {
    --backdrop: #0f1519;
    --card-dark: #07090b;
    --card-light: #ffffff;
    --ink-light: #ffffff;
    --ink-dark: #111111;
    --accent-red: #b3121a;
  }
  * { margin: 0; padding: 0; box-sizing: border-box; }
  html, body {
    width: 960px;
    height: 1200px;
    overflow: hidden;
    background: var(--backdrop);
    font-family: "Teko", "Arial Narrow", sans-serif;
  }
  .canvas {
    position: relative;
    width: 960px;
    height: 1200px;
  }
  .card {
    position: absolute;
  }
  .card--cover {
    left: 10px; top: 34px;
    width: 919px; height: 530px;
    background: var(--card-dark);
  }
  .card--contact {
    left: 0; top: 638px;
    width: 466px; height: 532px;
    background: var(--card-light);
  }
  .card--brand {
    left: 466px; top: 638px;
    width: 462px; height: 532px;
    background: var(--card-dark);
  }
  .brand-block {
    position: absolute;
    left: 0; right: 0;
    text-align: center;
    color: var(--ink-light);
    text-transform: uppercase;
  }
  .card--cover .brand-block { top: 204px; }
  .card--brand .brand-block { top: 208px; }
  .brand-name {
    font-weight: 500;
    line-height: 1;
    letter-spacing: 0.5px;
  }
  .card--cover .brand-name { font-size: 76px; }
  .card--brand .brand-name { font-size: 62px; }
  .brand-tagline {
    font-weight: 400;
    line-height: 1;
  }
  .card--cover .brand-tagline { font-size: 35px; margin-top: 20px; }
  .card--brand .brand-tagline { font-size: 28px; margin-top: 22px; }

  .person-name {
    position: absolute;
    left: 32px; top: 674px;
    font-size: 62px;
    font-weight: 400;
    line-height: 1;
    color: var(--ink-dark);
    text-transform: uppercase;
    letter-spacing: 1px;
  }
  .person-role {
    position: absolute;
    left: 32px; top: 732px;
    font-size: 21px;
    font-weight: 400;
    color: var(--accent-red);
    text-transform: uppercase;
    letter-spacing: 0.5px;
  }
  .contact-list {
    position: absolute;
    left: 34px; top: 1011px;
    list-style: none;
  }
  .contact-list li {
    display: flex;
    align-items: baseline;
    height: 44px;
    text-transform: uppercase;
  }
  .contact-label {
    width: 38px;
    font-size: 32px;
    font-weight: 500;
    color: var(--accent-red);
  }
  .contact-value {
    font-size: 26px;
    font-weight: 500;
    color: var(--ink-dark);
    letter-spacing: 0.3px;
  }
</style>
</head>
<body>
  <main class="canvas">
    <section class="card card--cover">
      <div class="brand-block">
        <div class="brand-name">Ironvale Motion</div>
        <div class="brand-tagline">Train like an athlete</div>
      </div>
    </section>

    <section class="card card--contact"></section>
    <h1 class="person-name">Corwin Maddock</h1>
    <p class="person-role">Personal trainer strength and conditioning coach</p>
    <ul class="contact-list">
      <li><span class="contact-label">P:</span><span class="contact-value">0491 572 806</span></li>
      <li><span class="contact-label">W:</span><span class="contact-value">www.ironvalemotion.com</span></li>
    </ul>

    <section class="card card--brand">
      <div class="brand-block">
        <div class="brand-name">Ironvale Motion</div>
        <div class="brand-tagline">Train like an athlete</div>
      </div>
    </section>
  </main>
</body>
</html>
```